Remodeling brochure

We need an informative homeowner friendly brochure detailing our company and things we do. We are looking for an initial setup and ideas (# of pages, etc) and then we will send more content. We are uploading our logo design. We are a high end remodeling company specializing in kitchen & bath remodels. We sell ourselves on customer communication and attention to detail in our designs and remodels.

Target Market(s)

Residential homeowners

Contact Information for Business Card

Modern and attention grabbing

Requirements
Must have
• Name- Hearth & Tile Crafters<br/>Address- 782 NW Larkspur Lane Suite #217<br/> Brookhaven, Ohio 50894<br/>Phone- 614-482-7395<br/>email-htcraftersmidwest@pinemail.net

```html
<!DOCTYPE html>
<html lang="en">
<head>
<meta charset="utf-8">
<title>Hearth &amp; Tile Crafters – Brochure Spreads</title>
<link href="https://fonts.googleapis.com/css2?family=Roboto:wght@300;400;700;900&display=swap" rel="stylesheet">
<style>
  :root{
    --canvas:#e4e5e8;
    --paper:#f4f4f5;
    --ink:#5b5d63;
    --navy:#1f2a7a;
    --blue:#1f74e0;
    --blue-light:#1d9de9;
    --blue-deep:#2b36b8;
    --charcoal:#2a2a2c;
    --offer-red:#e2242b;
    --page-dot:#8fc5f0;
    --page-dot-dark:#2c6fb0;
  }
  *{box-sizing:border-box;margin:0;padding:0}
  html,body{width:840px;height:1200px;overflow:hidden}
  body{background:var(--canvas);font-family:"Roboto",Arial,sans-serif;position:relative}

  .spread{position:absolute;left:10px;width:820px;height:264px;box-shadow:0 2px 6px rgba(0,0,0,.25);overflow:hidden}
  .spread--outside{top:321px}
  .spread--inside{top:615px}
  .panel{position:absolute;top:0;width:205px;height:264px;overflow:hidden}
  .panel--p1{left:0}
  .panel--p2{left:205px;border-left:1px solid rgba(0,0,0,.08)}
  .panel--p3{left:410px}
  .panel--p4{left:615px}

  .photo{position:absolute;display:block}
  .photo--kitchen-white{background:linear-gradient(160deg,#fbfbfb 0%,#e3e4e6 45%,#9a9ea4 100%)}
  .photo--kitchen-island{background:linear-gradient(180deg,#f2f2f3 0%,#d9dadc 45%,#6b5448 72%,#c8c0b6 100%)}
  .photo--open-plan{background:linear-gradient(165deg,#fafafa 0%,#dcdcdc 40%,#7c6a5e 80%,#4a3c33 100%)}

  .body-copy{font-size:5.4px;line-height:1.55;color:var(--ink);font-weight:400;text-align:justify}
  .body-copy + .body-copy{margin-top:5px}
  .body-copy--light{color:#f0f3ff}
  .body-copy--dark{color:#c9c9cc}

  .page-no{position:absolute;bottom:4px;width:12px;height:12px;border-radius:50%;background:var(--page-dot);color:#fff;font-size:6px;font-weight:700;text-align:center;line-height:12px}
  .page-no--left{left:6px}
  .page-no--right{right:6px}
  .page-no--dark{background:var(--page-dot-dark)}

  /* outside spread */
  .panel--service{background:var(--paper)}
  .panel--service .photo{left:12px;top:12px;width:181px;height:100px}
  .service-title{position:absolute;left:12px;top:124px;font-size:7.4px;font-weight:700;color:var(--navy);line-height:1.25}
  .panel--service .body-copy{position:absolute;left:12px;right:12px;top:148px}
  .panel--about{background:var(--paper);padding:12px}

  .panel--back,.panel--front{background:var(--charcoal)}
  .cover-art{position:absolute;inset:0}
  .brand{display:flex;align-items:center;gap:6px}
  .brand-mark{width:14px;height:14px;background:var(--blue);flex:none}
  .brand-name{font-weight:700;color:var(--blue);text-transform:uppercase;letter-spacing:.06em;line-height:1.15}
  .panel--front .brand{position:absolute;left:22px;top:54px}
  .panel--front .brand-name{font-size:11px}
  .back-contact{position:absolute;left:10px;right:8px;bottom:14px;display:flex;align-items:center;gap:6px}
  .back-contact .brand-name{font-size:5.6px;width:58px}
  .back-address{border-left:1px solid #66676b;padding-left:6px;font-size:4.6px;line-height:1.45;color:#cfd0d3;font-style:normal}

  /* inside spread */
  .inside-blue{position:absolute;left:0;top:0;width:410px;height:264px;background:linear-gradient(180deg,var(--blue-light) 0%,var(--blue) 45%,var(--blue-deep) 100%)}
  .blue-heading{position:absolute;top:12px;font-size:7.2px;font-weight:700;color:#fff;line-height:1.3}
  .blue-heading span{display:block;font-weight:300;font-size:7px}
  .blue-heading--left{left:12px}
  .blue-heading--right{left:12px;right:12px;text-align:left}
  .blue-heading--right span{text-align:right}
  .inside-photo{position:absolute;left:102px;top:40px;width:206px;height:152px}
  .col{position:absolute;top:42px}
  .col--left{left:12px;width:84px}
  .col--right{left:315px;width:82px}
  .foot{position:absolute;top:200px;width:181px}
  .foot--left{left:12px}
  .foot--right{left:217px}

  .panel--island{background:var(--charcoal)}
  .panel--island .photo{inset:0}

  .panel--offer{background:var(--charcoal);padding:12px}
  .offer-badge{display:inline-block;border:1px dashed var(--offer-red);padding:1px 4px;font-size:13px;font-weight:900;color:#fff;letter-spacing:.01em}
  .offer-sub{margin-top:6px;margin-bottom:8px;font-size:7.6px;font-weight:300;color:#fff;line-height:1.25;text-transform:uppercase}
</style>
</head>
<body>

<section class="spread spread--outside">
  <article class="panel panel--p1 panel--service">
    <div class="photo photo--kitchen-white" role="img" aria-label="Photo of a bright white kitchen with marble island and pendant lights"></div>
    <h2 class="service-title">Excellent Quality of<br>Workmanship &amp; Best Service</h2>
    <p class="body-copy">Every project begins with a conversation about how your family lives, cooks and unwinds. We listen first, sketch second, and keep you informed at each step so nothing about your new space ever comes as a surprise.</p>
  </article>

  <article class="panel panel--p2 panel--about">
    <p class="body-copy">Our designers pair durable materials with careful detailing, from aligned tile joints to soft-close drawers. Crews arrive on time, protect your floors and leave the site tidy at the end of every working day.</p>
    <p class="body-copy">Weekly updates, a single point of contact and a clear schedule mean you always know what happens next. Questions are answered the same day, and changes are priced before any work moves forward.</p>
    <p class="body-copy">Licensed, insured and backed by a written warranty on labor and finishes.</p>
    <span class="page-no page-no--left">3</span>
  </article>

  <article class="panel panel--p3 panel--back">
    <svg class="cover-art" viewBox="0 0 205 264" preserveAspectRatio="none" aria-hidden="true">
      <defs>
        <linearGradient id="backPhoto" x1="0" y1="0" x2="0" y2="1">
          <stop offset="0" stop-color="#f6f6f6"/><stop offset=".55" stop-color="#d2d3d5"/><stop offset="1" stop-color="#4c3e36"/>
        </linearGradient>
      </defs>
      <path d="M0 0H205V168Q110 176 0 214Z" fill="#1f74e0"/>
      <path d="M0 0H205V158Q110 166 0 204Z" fill="url(#backPhoto)"/>
    </svg>
    <div class="photo" role="img" aria-label="Photo of a white kitchen with island and chandeliers" style="left:0;top:0;width:205px;height:150px"></div>
    <div class="back-contact">
      <div class="brand-name">Hearth &amp; Tile Crafters</div>
      <address class="back-address">782 NW Larkspur Lane Suite #217<br>Brookhaven, Ohio 50894<br>Phone: 614-482-7395<br>htcraftersmidwest@pinemail.net</address>
    </div>
    <span class="page-no page-no--right page-no--dark">2</span>
  </article>

  <article class="panel panel--p4 panel--front">
    <svg class="cover-art" viewBox="0 0 205 264" preserveAspectRatio="none" aria-hidden="true">
      <defs>
        <radialGradient id="frontGlow" cx=".5" cy=".35" r=".6">
          <stop offset="0" stop-color="#4a4a4d"/><stop offset="1" stop-color="#2a2a2c"/>
        </radialGradient>
        <linearGradient id="frontPhoto" x1="0" y1="0" x2="0" y2="1">
          <stop offset="0" stop-color="#f5f5f4"/><stop offset=".6" stop-color="#cfcac4"/><stop offset="1" stop-color="#5a4a3f"/>
        </linearGradient>
      </defs>
      <rect width="205" height="264" fill="url(#frontGlow)"/>
      <path d="M0 160Q95 128 205 128V264H0Z" fill="#1f74e0"/>
      <path d="M0 168Q95 138 205 140V264H0Z" fill="url(#frontPhoto)"/>
    </svg>
    <div class="photo" role="img" aria-label="Photo of an open dining room and kitchen with dark wood floors" style="left:0;top:150px;width:205px;height:114px"></div>
    <div class="brand">
      <span class="brand-mark"></span>
      <span class="brand-name">Hearth &amp; Tile<br>Crafters</span>
    </div>
  </article>
</section>

<section class="spread spread--inside">
  <div class="inside-blue"></div>

  <article class="panel panel--p1">
    <h2 class="blue-heading blue-heading--left">Complete Kitchen &amp; Bath Remodeling<span>by Top Professionals</span></h2>
    <span class="page-no page-no--right">2</span>
  </article>

  <article class="panel panel--p2">
    <h2 class="blue-heading blue-heading--right">Complete Kitchen &amp; Bath Remodeling<span>by Top Professionals</span></h2>
    <span class="page-no page-no--left">3</span>
  </article>

  <div class="col col--left">
    <p class="body-copy body-copy--light">Kitchens, baths and laundry rooms planned around the way you move through the day, with storage where you need it most and lighting that makes every surface shine.</p>
  </div>
  <div class="inside-photo photo--open-plan" role="img" aria-label="Photo of an open-plan kitchen and living area spanning the fold"></div>
  <div class="col col--right">
    <p class="body-copy body-copy--light">Custom vanities, curbless showers, heated floors and quartz counters fitted with precision and finished to last for many years of daily family use.</p>
  </div>
  <div class="foot foot--left">
    <p class="body-copy body-copy--light">Full gut remodels or simple refreshes, handled by one trusted team from first sketch to final walkthrough.</p>
  </div>
  <div class="foot foot--right">
    <p class="body-copy body-copy--light">Schedule a free design visit and see samples, layouts and pricing in your own home.</p>
  </div>

  <article class="panel panel--p3 panel--island">
    <div class="photo photo--kitchen-island" role="img" aria-label="Photo of a white kitchen with dark wood island and upholstered stools"></div>
    <span class="page-no page-no--right page-no--dark">4</span>
  </article>

  <article class="panel panel--p4 panel--offer">
    <div class="offer-badge">SAVE 35% + 5%</div>
    <p class="offer-sub">On select cabinetry<br>&amp; free faucet</p>
    <p class="body-copy body-copy--dark">Book your kitchen remodel this season and save on select cabinet lines, plus receive a premium faucet at no added cost when your design is approved.</p>
    <p class="body-copy body-copy--dark">Offer applies to new contracts signed before the end of the quarter. Discount cannot be combined with other promotions. Ask our team for full details during your consultation.</p>
    <span class="page-no page-no--left page-no--dark">5</span>
  </article>
</section>

</body>
</html>
```